Brick lantern real estate investment company needs a poster design

We would like a poster design size 18 x 24.
Poster wording -
I WANT TO BUY YOUR ( finish with logo) logo uploaded
website- www.bricklantern.example
phone # 555-817-2643 ( color red for the phone number)
we would like to see the poster on 2 different backgrounds
Yellow background
White background
horizontal

```html
<!DOCTYPE html>
<html lang="en">
<head>
<meta charset="UTF-8">
<title>Brick lantern — Poster</title>
<link rel="stylesheet" href="https://fonts.googleapis.com/css2?family=Montserrat:wght@500;800&display=swap">
<style>
  :root {
    --backdrop: #8a8a8a;
    --paper: #ffffff;
    --ink: #111111;
    --accent: #e5232e;
  }
  * { margin: 0; padding: 0; box-sizing: border-box; }
  html, body {
    width: 1200px;
    height: 1200px;
    overflow: hidden;
    background: var(--backdrop);
  }
  .poster {
    position: absolute;
    left: 0;
    top: 136px;
    width: 1200px;
    height: 927px;
    background: var(--paper);
    font-family: "Montserrat", Arial, sans-serif;
    color: var(--ink);
  }
  .headline {
    position: absolute;
    top: 178px;
    width: 100%;
    text-align: center;
    font-weight: 500;
    font-size: 88px;
    line-height: 1;
    letter-spacing: 1px;
  }
  .headline .highlight {
    color: var(--accent);
    font-weight: 800;
  }
  .brand {
    position: absolute;
    top: 430px;
    width: 100%;
    display: flex;
    justify-content: center;
    align-items: center;
    gap: 28px;
  }
  .brand-mark {
    width: 70px;
    height: 70px;
    background: var(--accent);
  }
  .brand-name {
    font-weight: 800;
    font-size: 108px;
    line-height: 1;
    text-transform: uppercase;
    color: var(--ink);
  }
  .phone {
    position: absolute;
    top: 690px;
    width: 100%;
    text-align: center;
    font-weight: 800;
    font-size: 98px;
    line-height: 1;
    color: var(--accent);
  }
  .website {
    position: absolute;
    top: 823px;
    width: 100%;
    text-align: center;
    font-weight: 500;
    font-size: 38px;
    line-height: 1;
    letter-spacing: 4px;
    color: var(--ink);
  }
</style>
</head>
<body>
  <main class="poster">
    <h1 class="headline">I WANT TO <span class="highlight">BUY</span> YOUR</h1>
    <div class="brand">
      <span class="brand-mark" aria-hidden="true"></span>
      <span class="brand-name">Brick lantern</span>
    </div>
    <p class="phone">555-817-2643</p>
    <p class="website">www.bricklantern.example</p>
  </main>
</body>
</html>
```